Walking Beside the Quiet River; A Study of Refuge, Purpose & Calling

I need a book cover, for the above book title. This is a journey of the heart to know the heart of God. I think on the text, Simple (see below graphic)
Black Lettering for Knowing.....Intimately
Gold lettering for God
Either gold or black for the subtitle; A Study of Refuge, Purpose, & Calling
I would like the below graphic idea only no photograph of a person,
and White background instead of black
Simple Font, like below graphic, but open to suggestions

Target Market(s)

not age specific, Every person has been given a heart to know God, we are taking the mystery out the process to understand God is Father, loving gracious, ever present, etc. If we know His heart, we realize He's not at a distance, He is there, an ever present help

Industry/Entity Type

Security

Requirements
Must have
• Title: Walking Beside the Quiet River; A Study of Refuge, Purpose, & Calling
• My name, Tom Pettigrew
Nice to have
• See Below Graphic

```html
<!DOCTYPE html>
<html lang="en">
<head>
<meta charset="utf-8">
<title>Walking Beside the Quiet River — Book Cover</title>
<link href="https://fonts.googleapis.com/css2?family=Lato:wght@700;900&display=swap" rel="stylesheet">
<style>
  :root {
    --ink: #333333;
    --gold: #d4ae38;
    --paper: #ffffff;
  }
  html, body {
    margin: 0;
    padding: 0;
    width: 793px;
    height: 1200px;
    overflow: hidden;
    background: var(--paper);
  }
  .cover {
    position: relative;
    width: 793px;
    height: 1200px;
    background: var(--paper);
    font-family: "Lato", "Gill Sans", Arial, sans-serif;
    color: var(--ink);
    overflow: hidden;
  }
  .book-title {
    margin: 0;
  }
  .title-line {
    position: absolute;
    left: 0;
    width: 100%;
    margin: 0;
    text-align: center;
    text-transform: uppercase;
    white-space: nowrap;
    line-height: 1;
    box-sizing: border-box;
  }
  .title-lead {
    top: 104px;
    font-size: 42px;
    font-weight: 900;
    letter-spacing: 0.14em;
    padding-left: 0.14em;
  }
  .title-key {
    top: 171px;
    font-size: 220px;
    font-weight: 900;
    color: var(--gold);
    letter-spacing: 0.01em;
  }
  .title-tail {
    top: 441px;
    font-size: 74px;
    font-weight: 900;
    letter-spacing: 0.42em;
    padding-left: 0.42em;
  }
  .author {
    position: absolute;
    left: 130px;
    width: 509px;
    top: 741px;
    height: 75px;
    margin: 0;
    border-top: 2px solid var(--gold);
    border-bottom: 2px solid var(--gold);
    display: flex;
    align-items: center;
    justify-content: center;
    box-sizing: border-box;
    font-size: 34px;
    font-weight: 900;
    text-transform: uppercase;
    letter-spacing: 0.28em;
    padding-left: 0.28em;
    white-space: nowrap;
  }
  .subtitle-band {
    position: absolute;
    left: 0;
    bottom: 0;
    width: 100%;
    height: 215px;
    background: var(--gold);
    display: flex;
    align-items: center;
    justify-content: center;
  }
  .subtitle {
    margin: 0;
    text-align: center;
    font-size: 42px;
    font-weight: 900;
    line-height: 1.25;
    text-transform: uppercase;
    letter-spacing: 0.03em;
    word-spacing: 0.12em;
    color: var(--ink);
  }
</style>
</head>
<body>
  <main class="cover">
    <h1 class="book-title">
      <span class="title-line title-lead">Walking Beside the</span>
      <span class="title-line title-key">Quiet</span>
      <span class="title-line title-tail">River</span>
    </h1>
    <p class="author">Tom Pettigrew</p>
    <section class="subtitle-band">
      <p class="subtitle">A Study of Refuge, Purpose,<br>&amp; Calling</p>
    </section>
  </main>
</body>
</html>
```